Quillrun Couriers Web design

Take a look at our existing website(www.qlnrun.com) and design a new one, plus coding and recreate an existing logo.

```html
<!DOCTYPE html>
<html lang="en">
<head>
<meta charset="utf-8">
<title>Quillrun Couriers</title>
<link href="https://fonts.googleapis.com/css2?family=Poppins:wght@400;500;600;700&display=swap" rel="stylesheet">
<style>
:root{
  --orange:#f7841e;
  --blue:#1e5aa8;
  --blue-dark:#0f4a99;
  --ink:#222;
  --text:#444;
  --grey-nav:#8a8a8a;
  --light:#f5f5f5;
  --dark:#262a35;
  --darker:#1f222b;
  --white:#fff;
}
*{margin:0;padding:0;box-sizing:border-box}
html,body{width:1200px;height:3417px;overflow:hidden}
body{position:relative;font-family:'Poppins',sans-serif;color:var(--text);background:var(--white)}
.abs{position:absolute}
a{color:inherit;text-decoration:none}

/* header */
.header{left:0;top:0;width:1200px;height:97px;background:var(--white)}
.brand{left:160px;top:28px;font-weight:700;font-size:25px;color:var(--blue);line-height:1.15;letter-spacing:.5px}
.brand small{display:block;font-size:15px;font-weight:600;letter-spacing:2px}
.top-contact{left:750px;top:14px;font-size:12px;color:var(--ink);display:flex;gap:8px;align-items:center;line-height:1.3}
.top-contact b{font-weight:600}
.btn-quote{left:928px;top:13px;width:109px;height:29px;border-radius:15px;background:var(--blue-dark);color:#fff;font-size:11px;font-weight:600;display:flex;align-items:center;justify-content:center}
.nav{left:382px;top:57px;width:818px;height:40px;background:var(--grey-nav);border-radius:20px 0 0 20px;display:flex;align-items:center;padding-left:30px;gap:32px}
.nav a{color:#fff;font-size:11.5px;position:relative}
.nav a.active::after{content:"";position:absolute;left:0;right:0;bottom:-13px;height:2px;background:var(--orange)}

/* hero */
.hero{left:0;top:97px;width:1200px;height:660px;background:linear-gradient(100deg,#1d2a3e 0%,#33465e 35%,#6e6a66 60%,#9b8e80 100%)}
.hero-title{left:162px;top:295px;font-size:42px;font-weight:600;color:#fff;line-height:1.18;letter-spacing:-.5px}
.hero-text{left:162px;top:400px;font-size:14px;color:#fff;line-height:1.75}
.btn-orange{background:var(--orange);color:#fff;border-radius:20px;display:flex;align-items:center;justify-content:center;font-weight:500}
.hero-btn{left:162px;top:468px;width:166px;height:37px;font-size:13px}
.arrow{width:48px;height:48px;border-radius:50%;background:var(--blue);border:2px solid #fff;display:flex;align-items:center;justify-content:center}
.hero-curve{left:0;top:580px}

/* welcome */
.welcome{left:0;top:745px;width:1200px;height:405px;background:var(--light);text-align:center}
.welcome h2{position:absolute;top:82px;width:100%;font-size:21px;font-weight:600;color:var(--ink)}
.welcome h2 span{color:var(--orange)}
.welcome .lead{position:absolute;top:126px;left:280px;width:640px;font-size:13px;color:var(--ink);line-height:1.6}
.welcome .body{position:absolute;top:183px;left:280px;width:640px;font-size:12px;line-height:1.78}
.btn-grey{left:531px;top:1021px;width:137px;height:37px;border-radius:19px;background:#7c7c7c;color:#fff;font-size:12.5px;font-weight:500;display:flex;align-items:center;justify-content:center}

/* services */
.eyebrow{width:1200px;text-align:center;font-size:16px;color:var(--blue)}
.eyebrow::before,.eyebrow::after{content:"";display:inline-block;width:34px;height:2px;background:var(--blue);vertical-align:middle;margin:0 14px}
.section-title{width:1200px;text-align:center;font-size:35px;font-weight:600;color:var(--ink)}
.card-img{width:231px;height:212px;box-shadow:0 4px 8px rgba(0,0,0,.15)}
.card-meta{width:231px;height:40px;border-left:3px solid var(--blue);padding-left:9px}
.card-meta h3{font-size:15.5px;font-weight:500;color:var(--ink);line-height:1.3}
.card-meta p{font-size:11px;color:var(--text)}
.card-go{position:absolute;right:0;top:6px;width:26px;height:26px;border:1.5px solid var(--orange);border-radius:50%;color:var(--orange);font-size:13px;display:flex;align-items:center;justify-content:center}

/* process */
.process{left:0;top:1720px;width:1200px;height:395px;background:#f3f3f3}
.process .label{position:absolute;top:56px;width:100%;text-align:center;color:var(--orange);font-size:14px}
.process h2{position:absolute;top:82px;width:100%;text-align:center;font-size:30px;font-weight:600;color:var(--ink)}
.process .bar{position:absolute;top:124px;left:574px;width:52px;height:2px;background:var(--orange)}
.step{width:169px;height:103px;background:#fff;box-shadow:0 2px 6px rgba(0,0,0,.06);text-align:center;font-size:13px;color:var(--ink)}
.step svg{margin-top:14px}
.step span{position:absolute;left:0;right:0;top:70px}

/* testimonials */
.testi{left:0;top:2115px;width:1200px;height:438px;background:linear-gradient(90deg,#2f66ad,#3a72b8 50%,#1f5aa6)}
.testi h2{position:absolute;top:66px;width:100%;text-align:center;color:#fff;font-size:29px;font-weight:700}
.quote-card{width:350px;height:115px;background:#fff;padding:28px 26px 0 52px;font-size:11.5px;line-height:1.75}
.quote-card::after{content:"";position:absolute;left:30px;bottom:-12px;border:12px solid transparent;border-bottom:0;border-top-color:#fff}
.quote-mark{position:absolute;left:20px;top:22px;font-size:34px;font-weight:700;color:var(--blue);line-height:1}
.author{display:flex;align-items:center;gap:14px;color:#fff;font-size:11px}
.avatar{width:44px;height:44px;border-radius:50%;background:linear-gradient(#c8b8a8,#8d7b6d);border:2px solid #fff}
.author b{font-weight:600;display:block}
.dots{left:584px;top:2472px;display:flex;gap:4px}
.dots i{width:6px;height:6px;border-radius:50%;border:1px solid #fff}
.dots i.on{background:var(--orange);border-color:var(--orange)}

/* quote form */
.quote-photo{left:150px;top:2585px;width:430px;height:418px;background:linear-gradient(100deg,#c8322f 0%,#c44 35%,#b7c7dd 65%,#9fb4d0 100%);border-radius:8px 8px 0 0}
.quote-title{left:624px;top:2643px;font-size:25px;font-weight:500;color:var(--ink)}
.field{border:1px solid #bbb;background:#fff;font-size:10.5px;color:#444;padding:0 12px;display:flex;align-items:center}
.field.msg{align-items:flex-start;padding-top:12px}
.send{left:620px;top:2899px;width:343px;height:34px;background:var(--orange);color:#fff;font-size:9.5px;font-weight:600;letter-spacing:.5px;display:flex;align-items:center;justify-content:center}

/* cta + footer */
.cta{left:0;top:3003px;width:1200px;height:92px;background:var(--dark)}
.cta p{position:absolute;left:248px;top:34px;color:#fff;font-size:17px}
.cta p b{font-weight:600}
.cta-btn{left:841px;top:3028px;width:137px;height:33px;background:var(--blue);color:#fff;font-size:10px;font-weight:600;display:flex;align-items:center;justify-content:center}
.footer{left:0;top:3095px;width:1200px;height:260px;background:var(--dark)}
.footer-brand{left:180px;top:3140px;color:#fff;font-weight:700;font-size:23px;line-height:1.15}
.footer-brand small{display:block;font-size:14px;font-weight:600;letter-spacing:2px}
.footer-about{left:180px;top:3222px;width:200px;font-size:9.5px;color:#ccc;line-height:1.7}
.vline{width:1px;height:175px;background:#444a58;top:3130px}
.fcol h4{font-size:15px;font-weight:500;color:#fff;position:relative}
.fcol h4::before{content:"";position:absolute;left:0;top:-14px;width:28px;height:2px;background:var(--orange)}
.fcol ul{list-style:none;margin-top:20px}
.fcol li{font-size:10.5px;color:#ccc;line-height:21px}
.contact-list li{display:flex;gap:10px;line-height:1.6;margin-bottom:10px}
.social{display:flex;gap:6px;margin-top:16px}
.social i{width:20px;height:20px;border-radius:50%;background:var(--blue)}
.news-line{width:130px;height:1px;background:#555;margin:20px 0 22px}
.news{display:flex;margin-top:18px}
.news span{width:120px;height:26px;background:#fff;font-size:9px;color:#777;padding:0 10px;display:flex;align-items:center}
.news b{width:26px;height:26px;background:var(--blue);display:flex;align-items:center;justify-content:center}
.bottom{left:0;top:3355px;width:1200px;height:62px;background:var(--darker);font-size:10.5px;color:#bbb}
.bottom .l{position:absolute;left:188px;top:22px}
.bottom .r{position:absolute;right:185px;top:22px}
</style>
</head>
<body>

<header class="abs header">
  <div class="abs brand">Quillrun Couriers<small>COURIERS</small></div>
  <div class="abs top-contact">
    <svg width="20" height="20" viewBox="0 0 24 24"><path d="M6 3l3 4-2 2c1 3 3 5 6 6l2-2 4 3-2 3C10 19 5 14 3 6z" fill="var(--blue)"/></svg>
    <div><b>0123 555 019 20</b><br>info@qlnrun.com</div>
  </div>
  <a class="abs btn-quote">GET A QUOTE</a>
  <nav class="abs nav">
    <a class="active">HOME</a><a>ABOUT US</a><a>SERVICES</a><a>RATES</a><a>CUSTOMER BENEFITS</a><a>LOGISTICS</a><a>CONTACT US</a>
  </nav>
</header>

<section class="abs hero" role="img" aria-label="Courier handing a cardboard parcel to a smiling customer"></section>
<div class="abs hero-title">PICK-UP WITHIN 15-30<br>MINUTES AFTER CALL</div>
<p class="abs hero-text">Lorem ipsum dolor sit amet, consectetur adipiscing elit nunc<br>at augue lacus. Mauris a congue arcu.</p>
<a class="abs btn-orange hero-btn">CONTACT US NOW</a>
<div class="abs arrow" style="left:41px;top:334px"><svg width="16" height="16" viewBox="0 0 16 16"><path d="M10 2L4 8l6 6" stroke="#fff" stroke-width="2.5" fill="none"/></svg></div>
<div class="abs arrow" style="left:1109px;top:334px"><svg width="16" height="16" viewBox="0 0 16 16"><path d="M6 2l6 6-6 6" stroke="#fff" stroke-width="2.5" fill="none"/></svg></div>
<svg class="abs hero-curve" width="1200" height="180" viewBox="0 0 1200 180">
  <path d="M0 56 Q560 260 1200 20 L1200 180 L0 180Z" fill="var(--light)"/>
  <path d="M0 56 Q560 260 1200 20" stroke="var(--orange)" stroke-width="5" fill="none"/>
  <rect x="591" y="74" width="18" height="26" rx="9" fill="none" stroke="#fff" stroke-width="2"/>
  <line x1="600" y1="80" x2="600" y2="86" stroke="#fff" stroke-width="2"/>
  <path d="M600 102v12M596 110l4 4 4-4" stroke="#555" stroke-width="1.5" fill="none"/>
</svg>

<section class="abs welcome">
  <h2>WELCOME TO <span>QUILLRUN COURIERS.</span></h2>
  <p class="lead">We are committed to providing professional messenger services to cater for the most important, emergency and time sensitive deliveries valuable to your company.</p>
  <p class="body">Our services range from scheduled local and long distance, same day<br>to all types of On Demand services. Our goal is to become a leader by showing reliability, integrity as well as competitive pricing. Our company is licensed, bonded and fully insured with commercial grade insurance.</p>
</section>
<a class="abs btn-grey">LEARN MORE</a>

<div class="abs eyebrow" style="left:0;top:1218px">Our Services</div>
<h2 class="abs section-title" style="left:0;top:1242px">What We Do</h2>

<div class="abs card-img" style="left:194px;top:1336px;background:linear-gradient(135deg,#4a6fa5,#b9c9dc 60%,#e6ebf1)" role="img" aria-label="Doctor with stethoscope at a desk"></div>
<div class="abs card-meta" style="left:194px;top:1565px"><h3>Hospital &amp; Medical</h3><p>Pick up and delivery</p><span class="card-go">»</span></div>

<div class="abs card-img" style="left:484px;top:1367px;background:linear-gradient(135deg,#dfe6e2,#9fb0b8 50%,#3e4f66)" role="img" aria-label="Business people shaking hands at a meeting"></div>
<div class="abs card-meta" style="left:484px;top:1596px"><h3>Banking &amp; Brokerage</h3><p>Pick up and delivery</p><span class="card-go">»</span></div>

<div class="abs card-img" style="left:775px;top:1336px;background:linear-gradient(135deg,#6b7f7a,#2f4a4c 50%,#c9cfd2)" role="img" aria-label="Woman reviewing legal documents"></div>
<div class="abs card-meta" style="left:775px;top:1565px"><h3>Legal Filings</h3><p>Pick up and delivery</p><span class="card-go">»</span></div>

<section class="abs process">
  <div class="label">OUR WORK PROCESS</div>
  <h2>HOW WE WORK</h2>
  <div class="bar"></div>
  <svg class="abs" style="left:0;top:0" width="1200" height="395">
    <path d="M330 160 Q390 110 445 160" stroke="var(--orange)" stroke-dasharray="3 3" fill="none"/>
    <path d="M440 156l5 5 1-7" stroke="var(--orange)" fill="none"/>
    <path d="M755 160 Q815 110 870 160" stroke="var(--orange)" stroke-dasharray="3 3" fill="none"/>
    <path d="M865 156l5 5 1-7" stroke="var(--orange)" fill="none"/>
    <path d="M543 305 Q600 340 655 298" stroke="var(--orange)" stroke-dasharray="3 3" fill="none"/>
    <path d="M648 298l7 0-2 6" stroke="var(--orange)" fill="none"/>
  </svg>
</section>
<div class="abs step" style="left:194px;top:1897px">
  <svg width="40" height="48" viewBox="0 0 40 48"><path d="M10 4l7 8-4 4c2 6 6 10 11 12l4-4 8 7-5 6C18 36 7 24 5 10z" fill="var(--blue)"/><path d="M8 38c6-2 10 8 18 4" stroke="var(--orange)" stroke-width="3" fill="none"/></svg>
  <span>Request a Call</span></div>
<div class="abs step" style="left:413px;top:1897px">
  <svg width="70" height="44" viewBox="0 0 70 44"><rect x="4" y="6" width="38" height="26" fill="var(--orange)"/><path d="M42 14h14l8 10v8H42z" fill="var(--orange)"/><circle cx="16" cy="34" r="5" fill="var(--blue)"/><circle cx="54" cy="34" r="5" fill="var(--blue)"/><circle cx="24" cy="18" r="7" fill="#fff"/><line x1="2" y1="40" x2="68" y2="40" stroke="var(--blue)" stroke-width="2"/></svg>
  <span>Pick-up Goods</span></div>
<div class="abs step" style="left:623px;top:1897px">
  <svg width="50" height="46" viewBox="0 0 50 46"><circle cx="38" cy="10" r="7" fill="none" stroke="var(--orange)" stroke-width="2"/><path d="M38 6v4h3" stroke="var(--orange)" stroke-width="2" fill="none"/><path d="M6 8l6 18h16l6 14" stroke="var(--blue)" stroke-width="5" fill="none"/><circle cx="16" cy="8" r="4" fill="var(--orange)"/></svg>
  <span>WAIT</span></div>
<div class="abs step" style="left:836px;top:1897px">
  <svg width="44" height="46" viewBox="0 0 44 46"><rect x="10" y="2" width="26" height="22" fill="var(--blue)"/><line x1="23" y1="2" x2="23" y2="24" stroke="var(--orange)" stroke-width="4"/><path d="M4 30h12l8 4h14v6H12l-8-2z" fill="var(--blue)"/></svg>
  <span>Deliver Your Product</span></div>

<section class="abs testi" role="img" aria-label="Courier delivering a parcel to a happy client, blue tinted">
  <h2>WHAT CLIENT SAY</h2>
</section>
<div class="abs quote-card" style="left:235px;top:2250px"><span class="quote-mark">“</span>The heights by great men reached kept attaine by sudden flight, but the while companion slept were tooiling upward in the night.</div>
<div class="abs quote-card" style="left:618px;top:2250px"><span class="quote-mark">“</span>The heights by great men reached kept attaine by sudden flight, but the while companion slept were tooiling upward in the night.</div>
<div class="abs author" style="left:252px;top:2390px"><div class="avatar" role="img" aria-label="Client portrait"></div><div><b>MARA DELL</b>Senior UI/UX Designer</div></div>
<div class="abs author" style="left:636px;top:2390px"><div class="avatar" role="img" aria-label="Client portrait"></div><div><b>THEO BRANDT</b>Senior UI/UX Designer</div></div>
<div class="abs dots"><i class="on"></i><i></i><i></i></div>

<div class="abs quote-photo" role="img" aria-label="Courier in red cap handing a box to a woman signing for it"></div>
<h2 class="abs quote-title">Request A Quote</h2>
<div class="abs field" style="left:622px;top:2712px;width:155px;height:33px">Your Name</div>
<div class="abs field" style="left:793px;top:2712px;width:171px;height:33px">Your Email</div>
<div class="abs field" style="left:622px;top:2758px;width:342px;height:33px">Subject</div>
<div class="abs field msg" style="left:622px;top:2805px;width:342px;height:83px">Your Message</div>
<a class="abs send">SEND REQUEST</a>

<section class="abs cta"><p>Have any question or <b>need any business consultation?</b></p></section>
<a class="abs cta-btn">CONTACT US NOW!!</a>

<footer class="abs footer"></footer>
<div class="abs footer-brand">Quillrun Couriers<small>COURIERS</small></div>
<p class="abs footer-about">Lorem ipsum dolor sit amet, consectetur adipiscing elit. Nullam sollicitudin tempor sem vitae pretium. Fusce ultricies mollis purus non rutrum.</p>
<div class="abs vline" style="left:393px"></div>
<div class="abs vline" style="left:560px"></div>
<div class="abs vline" style="left:815px"></div>
<div class="abs fcol" style="left:446px;top:3145px"><h4>Site Links</h4>
  <ul><li>Home</li><li>About Us</li><li>Services</li><li>Rates</li><li>Contact Us</li></ul></div>
<div class="abs fcol" style="left:603px;top:3145px;width:200px"><h4>Contact Us</h4>
  <ul class="contact-list">
    <li><svg width="14" height="14" viewBox="0 0 24 24"><path d="M6 3l3 4-2 2c1 3 3 5 6 6l2-2 4 3-2 3C10 19 5 14 3 6z" fill="none" stroke="#ccc" stroke-width="1.6"/></svg>Phone: 123 555 01987</li>
    <li><svg width="14" height="14" viewBox="0 0 24 24"><path d="M12 22s7-7 7-12a7 7 0 0 0-14 0c0 5 7 12 7 12z" fill="none" stroke="#ccc" stroke-width="1.6"/><circle cx="12" cy="10" r="2.5" fill="none" stroke="#ccc" stroke-width="1.6"/></svg><span>Address: 48 Harbor Lane, Suite 9,<br>Fairview, NY</span></li>
    <li><svg width="14" height="14" viewBox="0 0 24 24"><rect x="3" y="6" width="18" height="13" fill="none" stroke="#ccc" stroke-width="1.6"/><path d="M3 6l9 7 9-7" fill="none" stroke="#ccc" stroke-width="1.6"/></svg>Email: mail@qlnrun.com</li>
  </ul></div>
<div class="abs fcol" style="left:870px;top:3145px"><h4>Get Connected</h4>
  <div class="social"><i></i><i></i><i></i></div>
  <div class="news-line"></div>
  <h4>Newsletter</h4>
  <div class="news"><span>Email...</span><b><svg width="12" height="12" viewBox="0 0 12 12"><path d="M1 6l10-5-3 10-2-4z" fill="#fff"/></svg></b></div>
</div>

<div class="abs bottom"><span class="l">@2021 Quillrun Couriers &nbsp;|&nbsp; All Rights Reserved.</span><span class="r">Terms &amp; Conditions &nbsp;|&nbsp; Privacy Policy</span></div>

</body>
</html>
```